"Paint every hour" App Design

Project goal is android app design. "Paint every hour" app is advising about using colors in everyday life to achieve goals, improve life, health, partnership, business and life overall. It is personalized to individual users. Recommendations are provided for personal and business environment, clothes, food etc. It is useful and fun.

Preferred design is clean, neat but special in a way to attract.

The app is functionally finished and ready for publishing. User will color a star/hexagram. This aspect (star) of the app is not subject of design and will remain the same. We are looking for design of all other pieces of the app, buttons, icons, font, icon, etc.

Hi! Based on the feedback we increased the budget. Please reconsider your response. Kind regards

```html
<!DOCTYPE html>
<html lang="en">
<head>
<meta charset="utf-8">
<title>Paint every hour – How to use</title>
<link rel="stylesheet" href="https://fonts.googleapis.com/css2?family=Fredoka:wght@600&family=Raleway:wght@400;500&display=swap">
<style>
  :root {
    --teal-light: #9fdde5;
    --teal: #4fc0cc;
    --teal-deep: #41b6c4;
    --status: #262626;
    --pink: #f2557a;
    --red-text: #e8305a;
    --grey-text: #8a8a8a;
    --star-grey: #dedede;
    --card: #ffffff;
    --bar: #f5e536;
    --muted: #8fd6de;
    --white: #ffffff;
  }
  * { box-sizing: border-box; margin: 0; padding: 0; }
  html, body { width: 782px; height: 1200px; overflow: hidden; }
  body {
    font-family: "Raleway", sans-serif;
    background: linear-gradient(160deg, var(--teal-light) 0%, var(--teal) 35%, var(--teal-deep) 100%);
    position: relative;
  }
  .status-bar {
    height: 46px; background: var(--status); color: var(--white);
    display: flex; justify-content: flex-end; align-items: center;
    gap: 10px; padding: 0 22px; font-size: 26px;
  }
  .status-bar svg { display: block; }
  .app-name {
    position: absolute; left: 0; top: 102px; width: 100%;
    text-align: center; line-height: 108px;
    font-family: "Fredoka", sans-serif; font-weight: 600;
    font-size: 80px; color: var(--pink); letter-spacing: -0.5px;
  }
  .intro {
    position: absolute; left: 71px; top: 222px; width: 640px;
    text-align: center; color: var(--white);
    font-size: 22px; line-height: 31px;
  }
  .guide-card {
    position: absolute; left: 37px; top: 335px; width: 709px; height: 747px;
    background: var(--card); border-radius: 6px;
    box-shadow: 0 5px 0 rgba(0,0,0,0.12);
  }
  .guide-title {
    position: absolute; left: 0; top: 34px; width: 100%;
    text-align: center; color: var(--grey-text);
    font-size: 22px; font-weight: 400; letter-spacing: 0.5px;
  }
  .star-art {
    position: absolute; left: 94px; width: 184px; height: 183px; border-radius: 4px;
  }
  .star-art.plain { top: 101px; background: var(--star-grey); }
  .star-art.coloured {
    top: 514px;
    background: linear-gradient(135deg, #6fb3ea 0%, #7fe0e0 40%, #f4dcd2 70%, #ef8cce 100%);
  }
  .swatches {
    position: absolute; left: 94px; top: 336px;
    display: grid; grid-template-columns: repeat(4, 46px); gap: 3px 10px;
  }
  .swatch { width: 46px; height: 46px; border-radius: 50%; }
  .step-label {
    position: absolute; left: 345px;
    color: var(--red-text); font-size: 30px; font-weight: 500; line-height: 36px;
  }
  .label-select { top: 145px; }
  .label-colour { top: 381px; }
  .label-finish { top: 577px; }
  .loading {
    position: absolute; left: 43px; top: 1114px; color: var(--muted); font-size: 24px;
  }
  .loading-bar { position: absolute; left: 44px; top: 1164px; display: flex; gap: 7px; }
  .loading-bar span { height: 5px; background: var(--bar); }
</style>
</head>
<body>
  <div class="status-bar">
    <svg width="70" height="26" viewBox="0 0 70 26" aria-hidden="true">
      <path d="M2 8 Q16 -4 30 8 L16 24 Z" fill="#fff"/>
      <path d="M34 24 L54 4 L54 24 Z" fill="#fff"/>
      <rect x="58" y="2" width="11" height="22" rx="1.5" fill="#fff"/>
    </svg>
    <span class="clock">12:06</span>
  </div>

  <h1 class="app-name">Paint every hour</h1>
  <p class="intro">"Paint every hour" is advising app about using colors in everyday life to achieve goals, improve life, health, partnership, business and life overall.</p>

  <section class="guide-card">
    <h2 class="guide-title">HOW TO USE THIS APP?</h2>

    <div class="star-art plain" role="img" aria-label="Grey star outline with one section highlighted and a tapping hand"></div>
    <p class="step-label label-select">Select a section in<br>the star</p>

    <div class="swatches">
      <span class="swatch" style="background:#3fb7e6"></span>
      <span class="swatch" style="background:#1592c9"></span>
      <span class="swatch" style="background:#96c61a"></span>
      <span class="swatch" style="background:#5f9612"></span>
      <span class="swatch" style="background:#f64c4c"></span>
      <span class="swatch" style="background:#d30d0d"></span>
      <span class="swatch" style="background:#fbb832"></span>
      <span class="swatch" style="background:#f7870c"></span>
      <span class="swatch" style="background:#b06fcf"></span>
      <span class="swatch" style="background:#9a2fcf"></span>
    </div>
    <p class="step-label label-colour">Choose a color</p>

    <div class="star-art coloured" role="img" aria-label="Star outline coloured in a blue to pink spectrum with a tapping hand"></div>
    <p class="step-label label-finish">Make it wonderful!</p>
  </section>

  <p class="loading">Checking License...</p>
  <div class="loading-bar">
    <span style="width:190px"></span>
    <span style="width:281px"></span>
    <span style="width:100px"></span>
    <span style="width:65px"></span>
  </div>
</body>
</html>
```